WedlockForge USA needs a Prayer booklet

I need a bookmark 2.5 x 8.5, full color, 2-sided, that lists a number of questions for married couples to ask themselves. The numbering is a little mixed up. Please make it look good.
My layout started with a different idea, but now would like it to be the shape of a larger bookmark.

Target Market(s)

Church

```html
<!DOCTYPE html>
<html lang="en">
<head>
<meta charset="utf-8">
<title>WedlockForge USA – Examination of Conscience Bookmark</title>
<link rel="stylesheet" href="https://fonts.googleapis.com/css2?family=Lobster&family=Cabin:ital,wght@0,400;1,400&family=Libre+Baskerville:wght@400;700&display=swap">
<style>
  :root{
    --page:#ffffff;
    --cream:#f6ecdf;
    --tan:#efc994;
    --sand:#e9d3b4;
    --rose:#e7b9b5;
    --script:#c2742e;
    --brown:#a9733f;
    --ink:#3b3a3a;
    --navy:#1d4f6e;
    --shadow:rgba(0,0,0,.35);
  }
  *{box-sizing:border-box;margin:0;padding:0}
  html,body{width:1200px;height:1200px;overflow:hidden;background:var(--page)}
  .canvas{position:relative;width:1200px;height:1200px}
  .spread{position:absolute;left:66px;width:1067px;display:flex;box-shadow:2px 3px 4px var(--shadow);background:var(--cream)}
  .spread--outside{top:66px;height:446px}
  .spread--inside{top:606px;height:444px}
  .panel{position:relative;width:50%;height:100%;overflow:hidden}
  .panel + .panel{border-left:1px dashed #c9b7a3}
  .photo{position:absolute;inset:0}

  /* outside back */
  .garden-photo{background:linear-gradient(160deg,#e3ddd6 0%,#d3cdc2 35%,#d9cdb9 60%,#e6cfc4 85%,#efe3d3 100%);opacity:.95}
  .script-title{font-family:"Lobster",cursive;color:var(--script);font-weight:400;text-align:center}
  .contrition-title{position:absolute;top:28px;left:0;right:0;font-size:27px}
  .prayer{position:absolute;top:64px;left:22px;right:22px;font-family:"Cabin",sans-serif;font-style:italic;font-size:15.5px;line-height:19px;color:var(--ink);text-align:center}
  .prayer .just{text-align:justify;text-align-last:justify}
  .logo-oval{position:absolute;left:121px;top:192px;width:282px;height:118px;border-radius:50%;background:#fff;display:flex;align-items:center;justify-content:center;gap:10px}
  .logo-oval .dot{width:16px;height:16px;border-radius:50%;background:var(--navy)}
  .logo-oval .brand{font-family:"Cabin",sans-serif;font-size:19px;color:var(--navy)}
  .order-note{position:absolute;top:318px;left:10px;right:10px;font-family:"Libre Baskerville",serif;font-weight:700;font-size:13px;line-height:18px;color:#1c1c1c;text-align:center}
  .order-note svg{vertical-align:-3px;margin:0 3px}
  .flourish{position:absolute;height:20px;width:150px;background:rgba(170,150,140,.35);border-radius:10px}
  .back .flourish{left:192px;top:396px}

  /* outside front */
  .front{background:var(--cream)}
  .front-art{position:absolute;inset:0}
  .front-title{position:absolute;left:0;right:0;top:372px;font-size:27px;line-height:35px}

  /* inside */
  .hands-photo{background:radial-gradient(ellipse at 55% 55%,#e9d6c8 0%,#efe5dc 45%,#f6f0ea 80%);}
  .stripe{position:absolute;top:0;bottom:0;background:var(--tan)}
  .q-list{position:absolute;list-style:none;font-family:"Cabin",sans-serif;font-size:15.5px;line-height:20px;color:var(--ink)}
  .q-list li{display:grid;grid-template-columns:27px 1fr;text-align:justify}
  .q-list .n{font-family:"Libre Baskerville",serif;font-size:13px}
  .inside-left .q-list{top:12px;left:12px;right:14px}
  .inside-right .q-list{top:8px;left:10px;right:22px}
  .inside-right .q-list li{line-height:21px}
  .blank-line{display:block;height:31px;background:#fff;margin-top:4px}
  .inside-left .flourish{left:196px;top:398px}
  .inside-right .flourish{left:192px;top:398px}
  .curve-bg{position:absolute;inset:0}
</style>
</head>
<body>
<div class="canvas">

  <section class="spread spread--outside">
    <div class="panel back">
      <div class="photo garden-photo" role="img" aria-label="Faded photograph of a garden with roses in front of a manor house"></div>
      <h2 class="script-title contrition-title">Act of Contrition</h2>
      <p class="prayer">
        O my God, I am heartily sorry for having offended you.<br>
        <span class="just" style="display:block">And I detest all my sins because of your just punishment.</span>
        But most of all because they offend you, my God, who art all-good<br>
        and deserving of all my love.<br>
        I firmly resolve, with the help of your grace, to sin no more, and to<br>
        avoid the near occasion of sin. Amen.
      </p>
      <div class="logo-oval"><span class="dot"></span><span class="brand">WedlockForge USA</span></div>
      <p class="order-note">
        Additional quantity copies of<br>
        AN EXAMINATION OF CONSCIENCE FOR THE MARRIED are available<br>
        from <svg width="14" height="14" viewBox="0 0 14 14"><circle cx="7" cy="7" r="6.5" fill="#1d4f6e"/><path d="M1 7h12M7 1c-3 3-3 9 0 12M7 1c3 3 3 9 0 12" stroke="#fff" stroke-width="1" fill="none"/></svg>www.wedlockforgeusa.org<br>
        or by contacting Dale &amp; Laurie Brenner at <svg width="14" height="14" viewBox="0 0 14 14"><rect width="14" height="14" rx="3" fill="#1d4f6e"/><path d="M4 3l2 2-1 1.5c.7 1.4 1.6 2.3 3 3L9.5 8l2 2-1.5 1.5C6.5 11 3 7.5 2.5 4.5z" fill="#fff"/></svg>(555) 014-0263.
      </p>
      <div class="flourish" role="img" aria-label="Ornamental flourish"></div>
    </div>

    <div class="panel front">
      <svg class="front-art" width="533" height="446" viewBox="0 0 533 446">
        <rect width="533" height="446" fill="#f6ecdf"/>
        <path d="M0 0H140C70 80 20 200 0 360Z" fill="#ecd9bf"/>
        <path d="M533 300V446H400C460 410 510 360 533 300Z" fill="#ecd9bf"/>
        <path d="M140 0H533V360H0C20 200 70 80 140 0Z" fill="#cfb08a" role="img" aria-label="Photograph of a couple seen from behind on a garden bench facing a palace"/>
        <path d="M60 170C200 40 380 10 533 0V30C380 40 220 80 60 170Z" fill="#e8b8b6" opacity=".8"/>
        <path d="M0 368C160 338 380 340 536 360" stroke="#b07a42" stroke-width="7" fill="none"/>
        <path d="M0 372H533V446H0Z" fill="#f7eee3" opacity=".6"/>
      </svg>
      <h1 class="script-title front-title">An Examination Of Conscience<br>For The Married</h1>
    </div>
  </section>

  <section class="spread spread--inside">
    <div class="panel inside-left">
      <div class="photo hands-photo" role="img" aria-label="Soft faded photograph of joined hands with wedding rings"></div>
      <div class="stripe" style="left:0;width:37px"></div>
      <ol class="q-list">
        <li><span class="n">1.</span><span>Have I said thoughtless or hurtful words, yelled indiscriminately, or in any other way been unkind or uncharitable to my spouse or family members?</span></li>
        <li><span class="n">2.</span><span>Have I been angry at my spouse?</span></li>
        <li><span class="n">3.</span><span>Have I allowed resentments and bitterness toward my spouse to take root in my mind?</span></li>
        <li><span class="n">4.</span><span>Has pride or selfishness caused me to stumble and fall short in my marriage?</span></li>
        <li><span class="n">5.</span><span>Do I have an attitude that I’m right and my spouse is always wrong?</span></li>
        <li><span class="n">6.</span><span>Have I been hard-hearted or callous?</span></li>
        <li><span class="n">7.</span><span>Have I been unfair, causing pain, resentment and hurt in my marriage?</span></li>
        <li><span class="n">8.</span><span>Are my priorities misplaced?</span></li>
        <li><span class="n">9.</span><span>Am I defensive or critical of my spouse, of my children?</span></li>
        <li><span class="n">10.</span><span>Have I been rude or self-seeking?</span></li>
        <li><span class="n">11.</span><span>Do I keep a record of wrongs?</span></li>
        <li><span class="n">12.</span><span>Have I been unsupportive?</span></li>
        <li><span class="n">13.</span><span>Have I spoken sharply or sarcastically to my spouse? Have I spoken in a demeaning or negative way?</span></li>
      </ol>
      <div class="flourish" role="img" aria-label="Ornamental flourish"></div>
    </div>

    <div class="panel inside-right">
      <svg class="curve-bg" width="533" height="444" viewBox="0 0 533 444">
        <rect width="533" height="444" fill="#fbf6f1"/>
        <path d="M440 0H533V444H360C470 330 520 160 440 0Z" fill="#efdcc4"/>
        <path d="M420 0C500 120 480 300 330 444H360C500 310 520 140 440 0Z" fill="#f5e6d6"/>
        <path d="M340 200C300 300 220 380 120 420C230 360 290 290 340 200Z" fill="#e8b8b6" opacity=".6"/>
      </svg>
      <div class="stripe" style="left:7px;width:27px"></div>
      <ol class="q-list" style="left:14px">
        <li><span class="n">14.</span><span>Have I failed to seek God’s plan for our marriage?</span></li>
        <li><span class="n">15.</span><span>Has infidelity, pornography, overspending occurred?</span></li>
        <li><span class="n">16.</span><span>Have I failed to follow the teachings of the Church on Family Planning?</span></li>
        <li><span class="n">17.</span><span>Have I failed to turn to God in prayer?</span></li>
        <li><span class="n">18.</span><span>Have I been unwilling to work to make our marriage healthy?</span></li>
        <li><span class="n">19.</span><span>Have I failed to protect my spouse?</span></li>
        <li><span class="n">20.</span><span>Have I been unwilling to make changes in my behavior? In my attitude? If so, what has been the consequences?</span></li>
        <li><span class="n">21.</span><span>Have I threatened to leave? Or avoided the problems I create?</span></li>
        <li><span class="n">22.</span><span>Have I told little lies, or big ones? Been imprecise in my words?</span></li>
        <li><span class="n">23.</span><span>Am I impatient with the ones I love?</span></li>
        <li><span class="n">24.</span><span>Have I physically abused my spouse?</span></li>
        <li><span class="n">25.</span><span>Have I gossiped about my spouse?</span></li>
        <li><span class="n">26.</span><span>Have I failed to seek forgiveness?</span></li>
        <li><span class="n">27.</span><span>Have I been unforgiving?</span></li>
        <li><span class="n">28.</span><span class="blank-line"></span></li>
      </ol>
      <div class="flourish" role="img" aria-label="Ornamental flourish"></div>
    </div>
  </section>

</div>
</body>
</html>
```